Building Company Business Card Design

I am looking to get a business card designed for my Building Company. Please find the logo attached.

Industry/Entity Type

Business

Contact Information for Business Card

Mobile 0472 913 046
Email admin@tarrowconstructworks.com.au
Website www.tarrowconstructworks.com.au

Colors
0255a3

```html
<!DOCTYPE html>
<html lang="en">
<head>
<meta charset="utf-8">
<title>Tarrow Construct Works – Business Card</title>
<link rel="stylesheet" href="https://fonts.googleapis.com/css2?family=Montserrat:wght@400;600;700&family=Open+Sans:wght@400;600&display=swap">
<style>
  :root {
    --page-bg: #0a4a9e;
    --brand-blue: #0255a3;
    --deep-blue: #0b3a7a;
    --bright-blue: #1f7fd6;
    --sky-blue: #2ea6e0;
    --white: #ffffff;
    --ink-grey: #4a4f57;
    --rule-grey: #c9ccd1;
  }
  * { box-sizing: border-box; margin: 0; padding: 0; }
  html, body { width: 1200px; height: 856px; overflow: hidden; }
  body {
    background: radial-gradient(ellipse at 50% 40%, #1560b5 0%, var(--page-bg) 55%, #07397d 100%);
    font-family: "Open Sans", Arial, sans-serif;
    display: flex;
    flex-direction: column;
    align-items: center;
    justify-content: center;
    gap: 40px;
  }
  .card {
    width: 620px;
    height: 354px;
    border-radius: 28px;
    position: relative;
    overflow: hidden;
    box-shadow: 0 14px 30px rgba(0, 20, 60, 0.35);
  }

  /* Front */
  .card-front {
    background: linear-gradient(120deg, #1a66c4 0%, var(--deep-blue) 45%, #1b6fc9 75%, var(--sky-blue) 100%);
  }
  .card-front .front-art { position: absolute; inset: 0; }
  .card-front .brand {
    position: absolute;
    left: 0; right: 0; top: 118px;
    text-align: center;
    font-family: "Montserrat", Arial, sans-serif;
    font-weight: 700;
    font-size: 40px;
    line-height: 1.1;
    letter-spacing: 1px;
    color: var(--white);
  }
  .card-front .web-tab {
    position: absolute;
    left: 205px; bottom: 0;
    width: 330px; height: 40px;
    background: var(--bright-blue);
    border-radius: 12px 12px 0 0;
    color: var(--white);
    font-weight: 600;
    font-size: 15px;
    display: flex; align-items: center; justify-content: center;
  }
  .card-front .edge-band {
    position: absolute; left: 0; right: 0; bottom: 0; height: 6px;
    background: var(--bright-blue);
  }

  /* Back */
  .card-back { background: var(--white); }
  .card-back .brand {
    position: absolute;
    left: 40px; top: 138px;
    width: 290px;
    font-family: "Montserrat", Arial, sans-serif;
    font-weight: 700;
    font-size: 26px;
    line-height: 1.15;
    color: var(--brand-blue);
  }
  .card-back .divider {
    position: absolute; left: 350px; top: 60px;
    width: 1.5px; height: 170px;
    background: var(--rule-grey);
  }
  .contact {
    position: absolute; left: 372px; top: 62px; width: 235px;
  }
  .contact .person {
    font-family: "Montserrat", Arial, sans-serif;
    font-weight: 700; font-size: 19px; color: var(--brand-blue);
  }
  .contact .role { font-size: 14px; color: var(--ink-grey); margin-bottom: 10px; }
  .contact-list { list-style: none; }
  .contact-list li {
    display: flex; align-items: flex-start; gap: 8px;
    font-size: 10.5px; line-height: 1.45; color: var(--ink-grey);
    margin-bottom: 5px;
  }
  .contact-list svg { flex: 0 0 12px; width: 12px; height: 12px; margin-top: 2px; fill: var(--brand-blue); }
  .card-back .edge-strip {
    position: absolute; left: 0; right: 0; bottom: 0; height: 10px;
    display: flex;
  }
  .edge-strip span { height: 100%; }
  .edge-strip .grey { background: var(--rule-grey); }
  .edge-strip .blue { background: var(--bright-blue); }
</style>
</head>
<body>

  <section class="card card-back" aria-label="Business card back">
    <div class="brand">Tarrow Construct Works</div>
    <div class="divider"></div>
    <div class="contact">
      <div class="person">Name Surname</div>
      <div class="role">Designation</div>
      <ul class="contact-list">
        <li>
          <svg viewBox="0 0 12 12"><path d="M6 0a4 4 0 0 0-4 4c0 3 4 8 4 8s4-5 4-8a4 4 0 0 0-4-4zm0 5.6A1.6 1.6 0 1 1 6 2.4a1.6 1.6 0 0 1 0 3.2z"/></svg>
          <span>#000 Calder Street, Kelsey Ponds, Victoria, 0000, Australia</span>
        </li>
        <li>
          <svg viewBox="0 0 12 12"><path d="M2.5 0.5l2 0 1 3-1.4 1a7 7 0 0 0 3.4 3.4l1-1.4 3 1v2a1.5 1.5 0 0 1-1.5 1.5A10 10 0 0 1 1 2 1.5 1.5 0 0 1 2.5 0.5z"/></svg>
          <span>0472 913 046</span>
        </li>
        <li>
          <svg viewBox="0 0 12 12"><path d="M0 2h12v8H0zM0.8 2.6 6 6.6l5.2-4v0.9L6 7.6 0.8 3.5z" fill-rule="evenodd"/></svg>
          <span>admin@tarrowconstructworks.com.au</span>
        </li>
        <li>
          <svg viewBox="0 0 12 12"><path d="M6 0a6 6 0 1 0 0 12A6 6 0 0 0 6 0zm0 1.2c.7.8 1.2 2 1.4 3.3H4.6C4.8 3.2 5.3 2 6 1.2zM1.3 5.5h2.3a9 9 0 0 0 0 1H1.3zm0 0M4.6 7.5h2.8C7.2 8.8 6.7 10 6 10.8 5.3 10 4.8 8.8 4.6 7.5zM1.3 6.5h2.3a9 9 0 0 0 .1 1H1.6a4.8 4.8 0 0 1-.3-1zm7.1-1h2.3v1H8.4a9 9 0 0 0 0-1zM4.5 5.5h3v1h-3z"/></svg>
          <span>www.tarrowconstructworks.com.au</span>
        </li>
      </ul>
    </div>
    <div class="edge-strip">
      <span class="grey" style="width:28%"></span>
      <span class="blue" style="width:22%"></span>
      <span class="grey" style="width:30%"></span>
      <span class="blue" style="width:20%"></span>
    </div>
  </section>

  <section class="card card-front" aria-label="Business card front">
    <div class="front-art" role="img" aria-label="Soft abstract blue background of layered translucent shapes"></div>
    <div class="brand">TARROW<br>CONSTRUCT WORKS</div>
    <div class="edge-band"></div>
    <div class="web-tab">www.tarrowconstructworks.com.au</div>
  </section>

</body>
</html>
```